Need a flyer for new tech startup

We are developing a new app that helps business owners streamline their efficiency when it comes to wages. The software is called PayVexa and it is composed of dashboards and reports on how the user's business and employees are performing.

We want a flyer created that is clean, smart, techy and fun. There should be placeholder text for title, h1, h2, body, call to action (sign up), etc. Images, backgrounds, transitions and breaks should also be present.

You can visit our website, payvexa.net, but I don't want too much taken from what we have online. We will likely be taking elements from this project and putting them on our website to better establish the branding.

Bonus points for the incorporation or play on light, lightbulb, darkness, etc. ;)

***Final deliverable must include a PSD file with individual layers. Thanks so much!

Tag words to describe our brand: streamline, efficiency, clockwork, profitability, reports, charts, dashboard, feedback, lightbulb, intelligence

Here is the UI that the back end of our software uses: https://demo.tilemorrow.net/plintakit-html-pro/index.html

```html
<!DOCTYPE html>
<html lang="en">
<head>
<meta charset="UTF-8">
<title>PayVexa Flyer</title>
<link href="https://fonts.googleapis.com/css2?family=Inter:wght@300;400;500;700;800&display=swap" rel="stylesheet">
<style>
:root{
  --page-bg:#8fbedc;
  --paper:#d4e9f7;
  --brand-blue:#2f59a6;
  --headline:#3d5ba8;
  --ink:#1d2d5a;
  --white:#ffffff;
  --illo-teal:#2ea8c9;
  --illo-soft:#b3d2e9;
  --illo-pale:#eef6fb;
}
*{margin:0;padding:0;box-sizing:border-box}
html,body{width:1200px;height:1200px;overflow:hidden}
body{background:var(--page-bg);font-family:'Inter',sans-serif;color:var(--ink);position:relative}
.flyer{position:absolute;left:152px;top:20px;width:896px;height:1160px;background:var(--paper);box-shadow:0 14px 30px rgba(30,60,100,.18)}
.brand{position:absolute;left:0;right:0;top:70px;display:flex;justify-content:center;align-items:center;gap:8px}
.brand-mark{width:14px;height:14px;border-radius:50%;background:var(--ink)}
.brand-name{font-size:32px;font-weight:700;color:var(--ink);letter-spacing:.5px}
.headline{position:absolute;left:0;right:0;top:150px;text-align:center;font-size:63px;font-weight:800;line-height:73px;color:var(--headline);letter-spacing:-.5px}
.hero-art{position:absolute;left:194px;top:315px;width:487px;height:365px;border-radius:10px;background:linear-gradient(135deg,var(--illo-pale) 0%,var(--illo-soft) 55%,var(--illo-teal) 100%)}
.intro{position:absolute;left:0;right:0;top:702px;text-align:center;font-size:14.5px;line-height:21px;color:var(--ink)}
.rule{position:absolute;left:184px;width:529px;top:768px;height:1px;background:var(--ink)}
.tag{position:absolute;left:141px;height:52px;background:var(--brand-blue);color:var(--white);font-weight:700;font-size:20px;display:flex;align-items:center;padding-left:17px}
.tag-features{top:827px;width:117px}
.tag-price{top:905px;width:84px}
.feature-list{position:absolute;top:824px;list-style:none;font-size:14.5px;line-height:20.7px;white-space:nowrap}
.feature-list li::before{content:"• "}
.feature-list.col-a{left:303px}
.feature-list.col-b{left:585px}
.price-amount{position:absolute;left:302px;top:906px;font-size:48px;line-height:56px;font-weight:300;color:var(--headline);letter-spacing:-1.5px}
.price-period{position:absolute;left:410px;top:922px;font-size:13.5px;line-height:18px}
.price-divider{position:absolute;left:499px;top:915px;width:1px;height:44px;background:var(--ink)}
.price-details{position:absolute;left:548px;top:919px;font-size:14.5px;line-height:21px}
.footer-band{position:absolute;left:0;right:0;top:1016px;height:144px;background:var(--brand-blue);color:var(--white)}
.cta-button{position:absolute;left:141px;top:46px;width:154px;height:52px;border:2px solid var(--white);display:flex;align-items:center;justify-content:center;font-weight:700;font-size:19px}
.cta-note{position:absolute;left:318px;top:50px;font-size:14.5px;line-height:21px}
.contact{position:absolute;left:570px;top:50px;font-size:14.5px;line-height:21px;list-style:none}
.contact li{display:flex;align-items:center;gap:9px}
.contact .icon{width:14px;height:14px;flex:none}
</style>
</head>
<body>
<main class="flyer">
  <div class="brand"><span class="brand-mark"></span><span class="brand-name">PayVexa</span></div>
  <h1 class="headline">Manage Your Service<br>Business Smarter!</h1>
  <div class="hero-art" role="img" aria-label="Illustration of a large wall clock with gears, a lightbulb and a megaphone, with two people working on laptops beside it"></div>
  <p class="intro">It’s time to turn on the lights, and that’s why we came up with PayVexa, your<br>real-time, deep-dive dashboard for the financial health of your service business.</p>
  <div class="rule"></div>

  <div class="tag tag-features">Features</div>
  <ul class="feature-list col-a">
    <li>Employee Feedback</li>
    <li>Gamification &amp; Incentive Deployment</li>
    <li>Deep Dive Reports</li>
  </ul>
  <ul class="feature-list col-b">
    <li>Cash is King!</li>
    <li>Crew Combo</li>
    <li>Timesheets Are Done!</li>
  </ul>

  <div class="tag tag-price">Price</div>
  <div class="price-amount">$50/</div>
  <div class="price-period">Per<br>Month</div>
  <div class="price-divider"></div>
  <div class="price-details">1-20 active employees<br>All access: full capability plan</div>

  <footer class="footer-band">
    <div class="cta-button">Sign up now!</div>
    <p class="cta-note">Signup now at payvexa.net<br>to start your free trial!</p>
    <ul class="contact">
      <li><svg class="icon" viewBox="0 0 14 14"><rect x="1" y="1" width="12" height="12" rx="2" fill="#fff"/></svg>Your Social Page</li>
      <li><svg class="icon" viewBox="0 0 14 14"><rect x="1" y="3" width="12" height="9" fill="#fff"/><path d="M1 3 L7 8 L13 3" fill="none" stroke="#2f59a6" stroke-width="1.3"/></svg>your_email@email.com</li>
    </ul>
  </footer>
</main>
</body>
</html>
```